Cold Pressed Juice Cleanse Brochure

We need to update our existing brochure (attached) with new photography. The wording can remain the same, however, on the CLEANSE ORDER page (panel 3), make these changes. You can also consult our website for additional design ideas. www.brightmarlowtonic.com.au

Upon waking, drink your first juice, and drink your next juice in order every two hours thereafter.

Harbour Cleanse. This is our most popular cleanse & perfect for those who want to balance great-tasting juices with high efficiency. This bundle includes:
1. Greens Smoothie
2. Ember Fizzwater or Spicy red
3. Green A
4. Red or Sweet Carrot
5. Green B
6. Either Silk Pour

Meadow Cleanse
Our most intense & lowest calorie cleanse - you get the maximum results in the minimum amount of time. This bundle includes:
1. Fern Kick or Celery
2. Ember Fizzwater
3. Green Smoothie
4. Green B
5. Green A
6. Oatbloom Drinkable

Hearth Cleanse
The organic Hearth Cleanse. We've curated a mixture of smoothies, cold-pressed juices, bone broth and nut mylks to keep you clean and warm through the winter months. The broth together with our Ember Fizzwater and Oatbloom Drinkable can all be gently heated on the stove to nourish you from the inside and out. This bundle includes:
1. Green Smoothie
2. Ember Fizzwater or Spicy Red
3. Sweet Carrot or Red
4. Organic Bone Broth
5. Green B
6. Either Silk Pour

We truly believe in our Cleanses and the results speak for themselves. NOURISH your body with antioxidant-rich juices. HELP your digestion and encourage a healthy balance of flora in your belly. ENJOY better overall well-being and weight loss.

Target Market(s)

25-60 year old M & F

Industry/Entity Type

Health And Wellness

Requirements
Must have
• The info on the existing brochure together with the new information listed in the project description.

```html
<!DOCTYPE html>
<html lang="en">
<head>
<meta charset="utf-8">
<title>Bright Marlow Cleanse Brochure</title>
<link href="https://fonts.googleapis.com/css2?family=EB+Garamond:ital,wght@0,400;0,500;0,600;1,400;1,500&display=swap" rel="stylesheet">
<style>
  :root{
    --canvas:#efefef;
    --panel:#e2e2e2;
    --panel-light:#f7f7f7;
    --ink:#1d1d1d;
    --ink-soft:#3a3a3a;
    --green:#3f9b3c;
    --leaf:#5f9c4a;
    --juice-red:#7a1f2e;
    --juice-orange:#e8642a;
  }
  *{box-sizing:border-box;margin:0;padding:0}
  html,body{width:1200px;height:1200px;overflow:hidden;background:var(--canvas)}
  body{font-family:"EB Garamond",Georgia,serif;color:var(--ink);position:relative}
  .spread{position:absolute;left:200px;width:800px;height:566px;display:flex;box-shadow:0 6px 18px rgba(0,0,0,.12)}
  .spread--inside{top:20px}
  .spread--outside{top:614px}
  .panel{position:relative;width:400px;height:566px;overflow:hidden;background:var(--panel)}
  .panel--light{background:var(--panel-light)}
  .photo{position:absolute;display:block}
  .accent{color:var(--green)}

  /* inside left: belief panel */
  .photo--fruit-row{left:0;top:0;width:400px;height:250px;background:linear-gradient(180deg,#f4f2f2 0%,#e9d9da 35%,#d9e6cf 60%,#f1ede6 100%)}
  .photo--red-bottle{left:40px;top:275px;width:160px;height:291px;border-radius:26px 26px 0 0;background:linear-gradient(180deg,#6d1a28 0%,#7a1f2e 30%,#e8642a 31%,#e8642a 100%)}
  .belief{position:absolute;left:220px;top:290px;width:165px;font-size:9.5px;line-height:1.3;color:var(--ink-soft)}
  .belief__title{font-size:30px;line-height:.95;font-weight:400;color:var(--ink);margin-bottom:8px}
  .belief__title .accent{display:block}
  .belief p{margin-bottom:7px}

  /* inside right: order page */
  .order{padding:22px 22px 0 22px}
  .order__title{font-size:34px;font-weight:500;line-height:1;margin-bottom:10px}
  .photo--green-bottle{right:-10px;top:-10px;width:80px;height:76px;border-radius:16px;background:linear-gradient(160deg,#2f5a22,#5cbf3c)}
  .cleanse{position:absolute;font-size:9.2px;line-height:1.25;color:var(--ink-soft)}
  .cleanse h2{font-size:19px;font-weight:500;color:var(--ink);line-height:1.05;margin-bottom:3px}
  .cleanse ol{padding-left:14px;margin-top:2px}
  .cleanse--harbour{left:170px;top:80px;width:210px}
  .cleanse--meadow{left:170px;top:226px;width:210px}
  .cleanse--hearth{left:22px;top:374px;width:240px}
  .photo--bundle{width:130px;height:64px;border-radius:6px;background:linear-gradient(90deg,#2f6a25 0%,#4e9a35 30%,#e07a2a 50%,#9a2230 65%,#c9a98f 100%)}
  .photo--bundle-harbour{left:22px;top:124px}
  .photo--bundle-meadow{left:22px;top:272px}
  .photo--bundle-hearth{left:268px;top:420px;background:linear-gradient(90deg,#7a1f2e 0%,#e8642a 35%,#b85a2b 55%,#2f6a25 80%,#b49680 100%)}

  /* outside left: tips */
  .photo--greenery{left:0;top:0;width:400px;height:160px;background:linear-gradient(180deg,#dfe6dc 0%,#c4d6bc 55%,#e2e2e2 100%)}
  .tips{position:absolute;left:28px;top:170px;width:350px}
  .tips__title{font-size:30px;font-weight:600;margin-bottom:10px}
  .tips__list{list-style:none}
  .tip{display:flex;gap:10px;font-size:12px;line-height:1.3;font-style:italic;margin-bottom:7px}
  .tip__label{flex:0 0 34px;color:var(--green);font-size:11px}
  .tips__promise{margin-top:12px;padding-top:6px;border-top:1px solid var(--ink);font-size:9.5px;font-style:italic;line-height:1.35}

  /* outside right: cover */
  .brand{position:absolute;right:28px;top:26px;display:flex;align-items:center;gap:8px}
  .brand__mark{width:22px;height:22px;border-radius:50%;background:var(--green)}
  .brand__name{font-size:26px;font-weight:500;color:var(--ink-soft)}
  .handle{position:absolute;right:28px;top:76px;display:flex;align-items:center;gap:6px;font-size:11px;color:var(--ink-soft)}
  .handle__dot{width:9px;height:9px;border-radius:2px;background:var(--ink-soft)}
  .photo--cover{left:0;top:100px;width:400px;height:466px;background:radial-gradient(circle at 62% 45%,#57b83a 0 18%,#d8cfc0 19% 34%,#ecebe8 35% 60%,#8fb07a 80%,#dcdcd8 100%)}
  .badge{position:absolute;left:250px;top:460px;width:64px;height:64px;border-radius:50%;background:var(--green);border:4px solid #fff}
</style>
</head>
<body>

<section class="spread spread--inside">
  <article class="panel panel--light panel--belief">
    <span class="photo photo--fruit-row" role="img" aria-label="Row of colourful juice bottles on white with scattered flowers and fruit"></span>
    <span class="photo photo--red-bottle" role="img" aria-label="Close-up of a red beetroot juice bottle with orange label"></span>
    <div class="belief">
      <h1 class="belief__title">We truly <span class="accent">believe</span></h1>
      <p>in our Cleanses and the results speak for themselves.</p>
      <p>NOURISH your body with antioxidant-rich juices.</p>
      <p>HELP your digestion and encourage a healthy balance of flora in your belly.</p>
      <p>ENJOY better overall well-being and weight loss.</p>
      <p>Upon waking, drink your first juice, and drink your next juice in order every two hours thereafter.</p>
    </div>
  </article>

  <article class="panel panel--order">
    <span class="photo photo--green-bottle" role="img" aria-label="Green smoothie bottle"></span>
    <div class="order">
      <h1 class="order__title">Order cleanse!</h1>
    </div>

    <span class="photo photo--bundle photo--bundle-harbour" role="img" aria-label="Six juice bottles of the Harbour Cleanse bundle"></span>
    <div class="cleanse cleanse--harbour">
      <h2>Harbour <span class="accent">Cleanse</span></h2>
      <p>This is our most popular cleanse &amp; perfect for those who want to balance great-tasting juices with high efficiency. This bundle includes:</p>
      <ol>
        <li>Greens Smoothie</li>
        <li>Ember Fizzwater or Spicy red</li>
        <li>Green A</li>
        <li>Red or Sweet Carrot</li>
        <li>Green B</li>
        <li>Either Silk Pour</li>
      </ol>
    </div>

    <span class="photo photo--bundle photo--bundle-meadow" role="img" aria-label="Six juice bottles of the Meadow Cleanse bundle"></span>
    <div class="cleanse cleanse--meadow">
      <h2>Meadow <span class="accent">Cleanse</span></h2>
      <p>Our most intense &amp; lowest calorie cleanse - you get the maximum results in the minimum amount of time. This bundle includes:</p>
      <ol>
        <li>Fern Kick or Celery</li>
        <li>Ember Fizzwater</li>
        <li>Green Smoothie</li>
        <li>Green B</li>
        <li>Green A</li>
        <li>Oatbloom Drinkable</li>
      </ol>
    </div>

    <div class="cleanse cleanse--hearth">
      <h2>Hearth <span class="accent">Cleanse</span></h2>
      <p>The organic Hearth Cleanse. We've curated a mixture of smoothies, cold-pressed juices, bone broth and nut mylks to keep you clean and warm through the winter months. The broth together with our Ember Fizzwater and Oatbloom Drinkable can all be gently heated on the stove to nourish you from the inside and out. This bundle includes:</p>
      <ol>
        <li>Green Smoothie</li>
        <li>Ember Fizzwater or Spicy Red</li>
        <li>Sweet Carrot or Red</li>
        <li>Organic Bone Broth</li>
        <li>Green B</li>
        <li>Either Silk Pour</li>
      </ol>
    </div>
    <span class="photo photo--bundle photo--bundle-hearth" role="img" aria-label="Hearth Cleanse bottles with a jar of bone broth"></span>
  </article>
</section>

<section class="spread spread--outside">
  <article class="panel panel--tips">
    <span class="photo photo--greenery" role="img" aria-label="Fresh green leaves and herbs on a light surface"></span>
    <div class="tips">
      <h1 class="tips__title">Cleanse Tips</h1>
      <ol class="tips__list">
        <li class="tip"><span class="tip__label">Tip 1</span><span>Start each day with a 250ml glass of warm lemon water to kick-start early morning hydration, alkalization and elimination.</span></li>
        <li class="tip"><span class="tip__label">Tip 2</span><span>Consume your juices at regular intervals throughout the day and finish each juice.</span></li>
        <li class="tip"><span class="tip__label">Tip 3</span><span>Shake before consuming and chew your juice like food to get the digestive enzymes working for you.</span></li>
        <li class="tip"><span class="tip__label">Tip 4</span><span>Exercise does wonders for distracting from hunger and clearing the head... Just keep moving!</span></li>
        <li class="tip"><span class="tip__label">Tip 5</span><span>Cleansing affects people differently with a variety of side effects that might arise including headaches nausea, fatigue and irritability. Breathe deeply and repeat... This too shall pass!</span></li>
      </ol>
      <p class="tips__promise">No added sugar | No concentrates | No preservatives | Dairy-Free<br>Australian made &amp; owned | Cold Pressed from 100% whole fruits &amp; vegetables</p>
    </div>
  </article>

  <article class="panel panel--light panel--cover">
    <div class="brand">
      <span class="brand__mark"></span>
      <span class="brand__name">brightmarlow</span>
    </div>
    <div class="handle"><span class="handle__dot"></span>@brightmarlowtonic</div>
    <span class="photo photo--cover" role="img" aria-label="Green smoothie bottle on a ceramic plate with limes, mint and linen"></span>
    <span class="badge"></span>
  </article>
</section>

</body>
</html>
```